Northlake Imaging Partners
Professional
DMS, RDCS
418 Pellwick Row
Irvine, CA 92606
tvasquell@northlakeimagingpartners.com
www.northlakeimagingpartners.com
Providing high quality ultrasound imaging service in the convenience of the Physician's office.
Increase in quality patient care.
Full body ultrasound 7 days a week
High qulity equipment
Professional staff
Quick turnearound
Your Diagnostic Imaging Specialist
Logo file for NIP stationary

```html
<!DOCTYPE html>
<html lang="en">
<head>
<meta charset="utf-8">
<title>Northlake Imaging Partners – Business Cards</title>
<link href="https://fonts.googleapis.com/css2?family=Ubuntu:wght@400;700&display=swap" rel="stylesheet">
<style>
  :root {
    --purple: #8f4fa8;
    --grey-band: #6d6d72;
    --grey-light: #c9c9cc;
    --card-white: #ffffff;
    --card-fog: #f1f1f3;
    --stage: #e6e4e1;
  }
  * { margin: 0; padding: 0; box-sizing: border-box; }
  html, body { width: 1200px; height: 911px; overflow: hidden; }
  body {
    background: var(--stage);
    font-family: "Ubuntu", Arial, sans-serif;
    position: relative;
  }
  .card {
    position: absolute;
    width: 420px;
    height: 250px;
    border-radius: 12px;
    overflow: hidden;
    box-shadow: 0 4px 14px rgba(0,0,0,0.18);
  }
  .card svg.backdrop { position: absolute; inset: 0; }

  .brand {
    position: absolute;
    display: flex;
    align-items: center;
    gap: 10px;
  }
  .brand-dot {
    width: 32px; height: 32px; border-radius: 50%;
    background: var(--purple);
    flex: none;
  }
  .brand-name {
    color: var(--purple);
    font-weight: 700;
    font-size: 20px;
    text-transform: uppercase;
    line-height: 1.1;
  }

  /* Front card */
  .card-front { left: 150px; top: 150px; background: var(--card-white); }
  .card-front .brand { left: 28px; top: 32px; }
  .contact {
    position: absolute;
    left: 130px;
    top: 162px;
    color: #fff;
    font-size: 9.5px;
    line-height: 1.5;
  }
  .web {
    position: absolute;
    left: 0; right: 0; bottom: 12px;
    text-align: center;
    color: #fff;
    font-size: 10px;
    font-weight: 700;
  }

  /* Back card */
  .card-back { left: 630px; top: 150px; background: var(--purple); }
  .card-back .brand { right: 26px; bottom: 30px; }
  .card-back .brand-name { color: #fff; text-align: right; }
  .card-back .brand-dot { background: #fff; }

  /* Light card */
  .card-light {
    left: 390px; top: 510px;
    background: linear-gradient(180deg, var(--card-white) 0%, var(--card-fog) 100%);
  }
  .card-light .brand { left: 0; right: 0; bottom: 30px; justify-content: center; }
  .card-light .brand-name { text-align: center; }
</style>
</head>
<body>

  <section class="card card-front" aria-label="Business card front">
    <svg class="backdrop" width="420" height="250" viewBox="0 0 420 250">
      <path d="M0 118 C 110 82, 250 70, 420 96 L420 250 L0 250 Z" fill="var(--grey-band)"/>
      <path d="M0 128 C 120 100, 260 92, 420 112 L420 250 L0 250 Z" fill="var(--grey-light)"/>
      <path d="M0 138 C 130 112, 270 104, 420 124 L420 250 L0 250 Z" fill="var(--purple)"/>
    </svg>
    <div class="brand">
      <span class="brand-dot"></span>
      <div class="brand-name">Northlake Imaging<br>Partners</div>
    </div>
    <div class="contact">
      418 Pellwick Row, Irvine, CA 92606<br>
      P: 949 555 0147 &nbsp;|&nbsp; F: 949 555 0182<br>
      E: tvasquell@northlakeimagingpartners.com
    </div>
    <div class="web">www.northlakeimagingpartners.com</div>
  </section>

  <section class="card card-back" aria-label="Business card back">
    <div class="brand">
      <div class="brand-name">Northlake Imaging<br>Partners</div>
      <span class="brand-dot"></span>
    </div>
  </section>

  <section class="card card-light" aria-label="Business card alternate">
    <div class="brand">
      <span class="brand-dot"></span>
      <div class="brand-name">Northlake Imaging<br>Partners</div>
    </div>
  </section>

</body>
</html>
```